Flyer für eine Zahnarztpraxis
Zielgruppe
Zahnarztpraxis, Zielgruppe sind Patienten im Erwachsenenalter
Aufgabenstellung
Den Text habe ich bereits geschrieben. Es soll ein DINA4 Flyer werden, mit sechs Seiten.

```html
<!DOCTYPE html>
<html lang="de">
<head>
<meta charset="utf-8">
<title>Vitamin D – Flyer Zahnarztpraxis Lindhagen</title>
<link rel="stylesheet" href="https://fonts.googleapis.com/css2?family=Lexend:wght@400;500;600&family=Figtree:wght@400;500&display=swap">
<style>
  :root {
    --page: #f6eddf;
    --panel: #f2e5d2;
    --teal: #22606b;
    --teal-panel: #2b6e78;
    --cream: #f4e9d8;
    --sun: #f0b429;
    --photo-light: #f4dfb8;
    --photo-dark: #c99a63;
  }
  * { box-sizing: border-box; margin: 0; padding: 0; }
  html, body { width: 800px; height: 1200px; overflow: hidden; }
  body {
    background: var(--page);
    font-family: "Figtree", sans-serif;
    color: var(--teal);
    position: relative;
  }
  .panel { position: absolute; }
  .panel-cover {
    left: 40px; top: 41px; width: 340px; height: 1118px;
    background: var(--panel);
    box-shadow: 0 2px 6px rgba(0,0,0,.08);
  }
  .cover-photo {
    width: 340px; height: 430px;
    background: radial-gradient(ellipse at 50% 40%, var(--photo-light) 0%, #e7c38f 55%, var(--photo-dark) 100%);
  }
  .headline {
    font-family: "Lexend", sans-serif;
    font-weight: 600;
    color: var(--teal);
  }
  .cover-title {
    position: absolute; left: 28px; top: 452px;
    font-size: 39px; line-height: 44px; letter-spacing: -0.3px;
  }
  .cover-subtitle {
    position: absolute; left: 28px; top: 598px; width: 300px;
    font-size: 23px; line-height: 31px; font-weight: 400;
  }
  .benefit-list { position: absolute; list-style: none; }
  .benefit-list li {
    position: absolute; left: 0; display: flex; align-items: center;
    font-size: 17px; white-space: nowrap;
  }
  .benefit-list svg { flex: none; }
  .cover-benefits { left: 24px; top: 0; }
  .cover-benefits li svg { width: 40px; height: 40px; margin-right: 26px; }
  .practice-mark {
    position: absolute; left: 28px; top: 1033px;
    display: flex; align-items: center; gap: 10px;
  }
  .practice-dot {
    width: 26px; height: 26px; border-radius: 50%;
    border: 2px solid var(--teal);
  }
  .practice-name {
    font-family: "Lexend", sans-serif; font-weight: 500;
    font-size: 17px; line-height: 22px; letter-spacing: 0.5px;
    text-transform: uppercase;
  }
  .practice-name .line-big { font-size: 22px; display: block; }

  .panel-facts {
    left: 420px; top: 41px; width: 341px; height: 557px;
    background: var(--panel);
    box-shadow: 0 2px 6px rgba(0,0,0,.08);
  }
  .facts-title {
    position: absolute; left: 26px; top: 27px;
    font-size: 34px; line-height: 38px;
  }
  .facts-dot {
    position: absolute; right: 36px; top: 28px;
    width: 46px; height: 46px; border-radius: 50%;
    border: 2px solid var(--teal);
  }
  .facts-rule {
    position: absolute; left: 26px; top: 160px; width: 292px;
    border-top: 1.5px solid var(--teal);
  }
  .facts-question {
    position: absolute; left: 26px; top: 184px;
    font-size: 25px; line-height: 32px;
  }
  .facts-benefits { left: 26px; top: 0; }
  .facts-benefits li { font-size: 16px; }
  .facts-benefits li svg { width: 32px; height: 32px; margin-right: 16px; }

  .panel-warning {
    left: 420px; top: 623px; width: 341px; height: 535px;
    background: var(--teal-panel);
    color: var(--cream);
  }
  .warning-title {
    position: absolute; left: 27px; top: 27px;
    font-family: "Lexend", sans-serif; font-weight: 600;
    font-size: 27px; color: var(--cream);
  }
  .warning-list {
    position: absolute; left: 27px; top: 78px; width: 300px;
    list-style: none;
  }
  .warning-list li {
    position: relative; padding-left: 26px;
    font-size: 21px; line-height: 36px; margin-bottom: 14px;
  }
  .warning-list li::before {
    content: ""; position: absolute; left: 2px; top: 15px;
    width: 6px; height: 6px; border-radius: 50%; background: var(--cream);
  }
  .warning-note {
    position: absolute; left: 30px; top: 308px;
    font-size: 19px; line-height: 42px;
  }
</style>
</head>
<body>

<section class="panel panel-cover">
  <div class="cover-photo" role="img" aria-label="Foto einer lächelnden Frau mit Tasse im warmen Sonnenlicht"></div>
  <h1 class="headline cover-title">Vitamin D –<br>mehr als nur<br>Sonnenvitamin</h1>
  <p class="cover-subtitle">Was Ihre Zähne und Ihr Körper jetzt brauchen könnten</p>
  <ul class="benefit-list cover-benefits">
    <li style="top:729px">
      <svg viewBox="0 0 40 40" fill="none" stroke="var(--sun)" stroke-width="2.2" stroke-linecap="round">
        <circle cx="20" cy="20" r="8"/>
        <path d="M20 3v6M20 31v6M3 20h6M31 20h6M8 8l4 4M28 28l4 4M8 32l4-4M28 12l4-4"/>
      </svg>
      Stärkt das Immunsystem
    </li>
    <li style="top:794px">
      <svg viewBox="0 0 40 40" fill="none" stroke="var(--sun)" stroke-width="2.2" stroke-linejoin="round">
        <path d="M6 12c2-4 8-4 10-1l10 8c3-1 8 1 7 6-1 3-4 3-5 2 1 4-3 7-6 4-2-2-1-4 0-5L12 18c-3 2-8 0-6-6z"/>
      </svg>
      Starke Knochen
    </li>
    <li style="top:856px">
      <svg viewBox="0 0 40 40" fill="none" stroke="var(--teal)" stroke-width="2.2" stroke-linecap="round" stroke-linejoin="round">
        <path d="M10 34V16c0-6 2-10 6-11 3 0 4 3 2 5l-3 2v8c3-4 10-4 13 0 3 4 1 10-4 14H10z"/>
      </svg>
      Muskelfunktion und Balance
    </li>
    <li style="top:926px">
      <svg viewBox="0 0 40 40" fill="none" stroke="var(--teal)" stroke-width="2.2" stroke-linejoin="round">
        <path d="M24 4L10 22h10l-4 14 14-18H20z"/>
      </svg>
      Gegen Müdigkeit und Lethargie
    </li>
  </ul>
  <div class="practice-mark">
    <span class="practice-dot"></span>
    <span class="practice-name">Zahnarztpraxis<span class="line-big">Lindhagen &amp; Team</span></span>
  </div>
</section>

<section class="panel panel-facts">
  <h2 class="headline facts-title">Vitamin D –<br>mehr als nur<br>Sonnenvitamin</h2>
  <span class="facts-dot"></span>
  <div class="facts-rule"></div>
  <h3 class="headline facts-question">Warum ist Vitamin D<br>so wichtig für den<br>Körper?</h3>
  <ul class="benefit-list facts-benefits">
    <li style="top:308px">
      <svg viewBox="0 0 32 32" fill="none" stroke="var(--teal)" stroke-width="1.8" stroke-linecap="round" stroke-linejoin="round">
        <path d="M16 3l11 4v8c0 7-5 12-11 14C10 27 5 22 5 15V7z"/><path d="M16 10v12M10 16h12"/>
      </svg>
      Stärkt Ihr Immunsystem
    </li>
    <li style="top:369px">
      <svg viewBox="0 0 32 32" fill="none" stroke="var(--teal)" stroke-width="1.8" stroke-linecap="round" stroke-linejoin="round">
        <path d="M8 28V13c0-5 2-8 5-9 2 0 3 2 1 4l-2 2v6c2-3 8-3 10 0 3 3 1 8-3 12H8z"/>
      </svg>
      Starke Knochen
    </li>
    <li style="top:429px">
      <svg viewBox="0 0 32 32" fill="none" stroke="var(--teal)" stroke-width="1.8" stroke-linecap="round" stroke-linejoin="round">
        <path d="M10 26c-3-3-4-8-2-12 2-5 8-7 12-4 3 2 4 6 2 9l-3 3v4"/><path d="M14 14c1-2 4-2 5 0"/>
      </svg>
      Muskelfunktion und Balance
    </li>
    <li style="top:491px">
      <svg viewBox="0 0 32 32" fill="none" stroke="var(--teal)" stroke-width="1.8" stroke-linejoin="round">
        <path d="M19 3L8 18h8l-3 11 11-15h-8z"/>
      </svg>
      Gegen Müdigkeit und Lethargie
    </li>
  </ul>
</section>

<section class="panel panel-warning">
  <h2 class="warning-title">Mangel</h2>
  <ul class="warning-list">
    <li>häufige Infekte und Schlappheit</li>
    <li>unerklärliche Zahnfleisch&shy;entzündung</li>
    <li>sensibles Zahnfleisch</li>
  </ul>
  <p class="warning-note">Ihr Lächeln braucht einen<br>gesunden Körper</p>
</section>

</body>
</html>
```